Tallowfern Letterheads Design

Hello, we have just upgraded this project for a guaranteed payment.

We are currently going through a re-branding exercise internally. Our logo is attached as a PDF file.

We are happy with our logo but would like to investigate how we can best apply the logo to our letterheads and compliment slips.

We are a quality printing company in England. Despite our name we are very professional and offer a personal service.

Our new website is under construction and here is a link to show you how it looks: http://tallowpress.marlwood.co.uk

The style must be professional and steer away from "tacky" otherwise it makes our company look very low budget and just a bit silly.

We would like to see elements of creativity though, so please, nothing too boring.

I have attached our new logo, there is an option for use on white or black.

Cheers
Tallowfern Team
Updates

Project Deadline Extended
Reason: We have increased the deadline due to an internal delay to things, we now have more time before we need anything to be printed.

Industry/Entity Type

Construction

Requirements
Must have
• IMPORTANT! Please do not tweak or change our logo in any way. A few designs show vast changes in the logo, this is not what we require. Please do not change the logo in any way. Thanks
Nice to have
• Classy but approachable. Elements of "quirky" would be nice to see.
Should not have
• A Tacky feel

```html
<!DOCTYPE html>
<html lang="en">
<head>
<meta charset="utf-8">
<title>Tallowfern Letterhead</title>
<link rel="stylesheet" href="https://fonts.googleapis.com/css2?family=Montserrat:wght@500;700&display=swap">
<style>
  :root {
    --ink-dark: #161c20;
    --paper: #ffffff;
    --brand-pink: #e6195f;
    --text-light: #ffffff;
  }
  html, body {
    margin: 0;
    padding: 0;
    overflow: hidden;
    background: var(--ink-dark);
  }
  .letterhead {
    position: relative;
    width: 927px;
    height: 1200px;
    background: var(--ink-dark);
    font-family: "Montserrat", Arial, sans-serif;
    overflow: hidden;
  }
  .writing-sheet {
    position: absolute;
    left: 108px;
    top: 55px;
    width: 710px;
    height: 986px;
    background: var(--paper);
  }
  .brand-block {
    position: absolute;
    left: 0;
    right: 0;
    top: 1058px;
    text-align: center;
    color: var(--text-light);
  }
  .brand-mark {
    display: block;
    width: 40px;
    height: 40px;
    margin: 0 auto 4px;
    border-radius: 50%;
    background: var(--brand-pink);
  }
  .brand-name {
    margin: 0;
    font-size: 32px;
    font-weight: 700;
    line-height: 1.1;
    letter-spacing: 0.2px;
  }
  .brand-tagline {
    margin: 0;
    font-size: 12px;
    font-weight: 500;
    line-height: 1.3;
  }
  .contact-line {
    margin: 2px 0 0;
    font-size: 12.5px;
    font-weight: 700;
    letter-spacing: 0.3px;
    color: var(--brand-pink);
  }
</style>
</head>
<body>
  <main class="letterhead">
    <section class="writing-sheet" aria-label="Letter body area"></section>
    <footer class="brand-block">
      <span class="brand-mark" aria-hidden="true"></span>
      <p class="brand-name">Tallowfern</p>
      <p class="brand-tagline">Quality Printing</p>
      <p class="contact-line">tallowfern.co.uk | 0208 555 0187 | sales@tallowfern.co.uk</p>
    </footer>
  </main>
</body>
</html>
```